Builder of high-end, expensive tables and other furniture

Build a website that represents what we do. I want a luxury feel that appeals to those who can afford our products. We build very high end tables and other furniture using trees that have fallen or are standing dead. We never cut living trees. Trees are harvested, milled, and kiln dried. Then that lumber is meticulously turned into fine furniture using the best equipment. Our furniture prices range from $1,000-$20,000.

Trying to figure out how to raise my spend.

```html
<!DOCTYPE html>
<html lang="en">
<head>
<meta charset="utf-8">
<title>Heartwood Tables LLC</title>
<link rel="stylesheet" href="https://fonts.googleapis.com/css2?family=Gelasio:wght@400;500&family=Poppins:wght@400;500;600&display=swap">
<style>
:root{
  --orange:#e8732a;
  --blue:#1d4f9c;
  --ink:#1a1a1a;
  --body:#333333;
  --muted:#555555;
  --grey-band:#f5f5f5;
  --card:#f3f3f3;
  --footer:#2b2b2b;
  --white:#ffffff;
}
*{box-sizing:border-box;margin:0;padding:0}
html,body{width:1200px;height:2903px;overflow:hidden}
body{position:relative;font-family:"Poppins",sans-serif;color:var(--body);background:var(--white)}
.abs{position:absolute}
.serif{font-family:"Gelasio",serif;font-weight:400}

/* hero */
.hero{left:0;top:0;width:1200px;height:600px;
  background:linear-gradient(180deg,#e6e2d8 0%,#d8cfbf 45%,#a89880 75%,#6f6455 100%)}
.hero-logo{left:0;width:1200px;top:50px;text-align:center;font-family:"Gelasio",serif;font-size:40px;color:var(--orange)}
.menu{left:1056px;top:62px;width:34px}
.menu span{display:block;height:3px;background:var(--white);margin-bottom:7px;border-radius:2px}
.menu span:nth-child(1){width:26px;margin-left:8px}
.menu span:nth-child(3){width:26px;margin-left:8px}
.arrow{top:283px;width:35px;height:35px}
.hero-title{left:0;width:1200px;top:436px;text-align:center;color:var(--white);font-size:64px;line-height:1}
.hero-rule{left:468px;top:529px;width:265px;height:2px;background:var(--white)}

/* section headings */
.section-title{left:0;width:1200px;text-align:center;font-size:48px;line-height:1}
.accent{color:var(--orange)}
.navy{color:var(--blue)}

/* about */
.about-title{left:112px;top:672px;font-size:48px;line-height:1}
.about-lead{left:112px;top:756px;font-size:15.5px;line-height:28px;color:var(--ink);font-weight:500;white-space:nowrap}
.about-body{left:112px;top:824px;width:500px;font-size:15.5px;line-height:28.3px;color:var(--body)}
.btn{background:var(--orange);color:var(--white);font-weight:600;font-size:15px;display:flex;align-items:center;justify-content:center}
.about-btn{left:112px;top:1024px;width:116px;height:43px}
.photo-frame{left:737px;top:685px;width:353px;height:405px;border:1px solid #cfcfcf;background:var(--white)}
.photo-dining{left:753px;top:667px;width:336px;height:409px;background:linear-gradient(160deg,#f0efec 0%,#e4e1dc 50%,#c99a6b 100%)}
.photo-chair{left:646px;top:911px;width:259px;height:227px;background:linear-gradient(150deg,#ece6de 0%,#ddd3c6 55%,#a87a4c 100%);outline:3px solid var(--white)}

/* products */
.card{top:1294px;width:312px;height:338px;background:var(--card)}
.card .pic{position:absolute;left:22px;top:36px;width:268px;height:170px;border-radius:6px}
.card .name{position:absolute;left:0;width:100%;top:250px;text-align:center;font-size:17px;color:var(--body);word-spacing:4px}
.card .price{position:absolute;left:0;width:100%;top:280px;text-align:center;font-size:19px;font-weight:600;color:var(--ink)}
.view-btn{left:543px;top:1675px;width:115px;height:43px}

/* how it works */
.band{left:0;top:1774px;width:1200px;height:532px;background:var(--grey-band)}
.step-circle{width:124px;height:124px;border-radius:50%;background:var(--white);box-shadow:0 4px 12px rgba(0,0,0,.12);display:flex;align-items:center;justify-content:center}
.step-icon{width:66px;height:54px;border-radius:6px;background:linear-gradient(180deg,var(--blue) 0%,var(--orange) 100%)}
.step-num{font-size:44px;font-weight:600;color:#d8d8d8;line-height:1}
.step-title{width:240px;text-align:center;font-size:18px;font-weight:500;color:var(--ink)}
.step-text{width:240px;text-align:center;font-size:14px;line-height:26px;color:var(--muted)}

/* newsletter */
.news-text{left:150px;width:900px;top:2414px;text-align:center;font-size:16px;line-height:28.5px;color:var(--body)}
.email{left:341px;top:2500px;width:380px;height:46px;border:1px solid #e2e2e2;box-shadow:0 2px 8px rgba(0,0,0,.06);padding-left:28px;display:flex;align-items:center;font-size:15.5px;color:#444}
.submit{left:743px;top:2502px;width:115px;height:43px}

/* footer */
.footer{left:0;top:2615px;width:1200px;height:288px;background:var(--footer)}
.footer-logo{left:113px;top:2704px;font-family:"Gelasio",serif;font-size:40px;color:var(--white);line-height:1;display:flex;align-items:center;gap:12px}
.footer-logo i{display:block;width:12px;height:12px;border-radius:50%;background:var(--white)}
.footer-head{font-size:15px;font-weight:500;letter-spacing:.3px;color:var(--white)}
.footer-list{list-style:none;font-size:14.5px;color:var(--white)}
.contact-line{display:flex;align-items:center;gap:10px;font-size:14.5px;color:var(--white);white-space:nowrap}
.contact-line svg{width:13px;height:13px;fill:var(--white);flex:none}
.copyright{left:0;width:1200px;top:2857px;text-align:center;font-size:14.5px;color:var(--white)}
</style>
</head>
<body>

<!-- hero -->
<section class="abs hero" role="img" aria-label="Dining room with a wooden table, black chairs and a rattan sideboard"></section>
<div class="abs hero-logo">Heartwood Tables</div>
<div class="abs menu" aria-label="Menu"><span></span><span></span><span></span></div>
<svg class="abs arrow" style="left:36px" viewBox="0 0 36 36" aria-label="Previous slide">
  <circle cx="18" cy="18" r="16.5" fill="none" stroke="#ffffff" stroke-width="1.6" opacity=".6"/>
  <path d="M26 18H10M16 12l-6 6 6 6" fill="none" stroke="#ffffff" stroke-width="1.6" opacity=".6"/>
</svg>
<svg class="abs arrow" style="left:1129px" viewBox="0 0 36 36" aria-label="Next slide">
  <circle cx="18" cy="18" r="16.5" fill="none" stroke="#ffffff" stroke-width="1.8"/>
  <path d="M10 18h16M20 12l6 6-6 6" fill="none" stroke="#ffffff" stroke-width="1.8"/>
</svg>
<h1 class="abs hero-title serif">Welcome to Heartwood Tables LLC</h1>
<div class="abs hero-rule"></div>

<!-- about -->
<h2 class="abs about-title serif"><span class="accent">About</span> <span class="navy">us</span></h2>
<p class="abs about-lead">We build very high end tables and other furniture using trees<br>that have fallen or are standing dead. We never cut living trees</p>
<p class="abs about-body">ed ut perspiciatis unde omnis iste natus error sit accusantium doloremque laudantium, totam rem aperiam, eaque ipsa quae ab illo inventore veritatis et quasi architecto beatae vitae dicta sunt explicabo. Nemo enim ipsavoluptatem quia voluptas sit aspernatur aut odit aut fugit, sed onsequuntur magni dolores eos qui ratione voluptatem sequi nesciunt.</p>
<div class="abs btn about-btn">Learn More</div>
<div class="abs photo-frame"></div>
<div class="abs photo-dining" role="img" aria-label="Bright dining room with a wooden table and white chairs"></div>
<div class="abs photo-chair" role="img" aria-label="Rattan armchair with a cream cushion"></div>

<!-- products -->
<h2 class="abs section-title serif" style="top:1198px"><span class="accent">Our</span> <span class="navy">products</span></h2>
<div class="abs card" style="left:112px">
  <div class="pic" role="img" aria-label="Pair of teak nesting side tables" style="background:radial-gradient(ellipse at 50% 35%,#d69a4a 0%,#c07a34 40%,#f3f3f3 72%)"></div>
  <div class="name">Luxury furniture</div><div class="price">$1,000</div>
</div>
<div class="abs card" style="left:444px">
  <div class="pic" role="img" aria-label="Hexagonal wood top side table with black legs" style="background:radial-gradient(ellipse at 50% 40%,#8a5a3c 0%,#3a3030 40%,#f3f3f3 70%)"></div>
  <div class="name">Luxury furniture</div><div class="price">$1,000</div>
</div>
<div class="abs card" style="left:778px">
  <div class="pic" role="img" aria-label="Round glass top table with a gold wire base" style="background:radial-gradient(ellipse at 50% 45%,#ddd6c6 0%,#d4bb82 40%,#f3f3f3 72%)"></div>
  <div class="name">Luxury furniture</div><div class="price">$1,000</div>
</div>
<div class="abs btn view-btn">View All</div>

<!-- how it works -->
<section class="abs band"></section>
<h2 class="abs section-title serif" style="top:1836px"><span class="accent">How</span> <span class="navy">it works</span></h2>

<div class="abs step-circle" style="left:158px;top:1924px"><div class="step-icon" role="img" aria-label="Fallen tree being cut"></div></div>
<div class="abs step-num" style="left:93px;top:2014px">01.</div>
<div class="abs step-title" style="left:100px;top:2063px">Trees are harvested</div>
<div class="abs step-text" style="left:100px;top:2097px">Lorem ipsum dolor sitnsectetur adipiscing elit, sed do eiusmod tempor incididunt ut labore et.</div>

<div class="abs step-circle" style="left:412px;top:1975px"><div class="step-icon" role="img" aria-label="Logs being milled into boards"></div></div>
<div class="abs step-num" style="left:362px;top:2076px">02.</div>
<div class="abs step-title" style="left:354px;top:2115px">Trees are milled</div>
<div class="abs step-text" style="left:354px;top:2149px">Lorem ipsum dolor sitnsectetur adipiscing elit, sed do eiusmod tempor incididunt ut labore et.</div>

<div class="abs step-circle" style="left:667px;top:1924px"><div class="step-icon" role="img" aria-label="Stacked lumber in a kiln"></div></div>
<div class="abs step-num" style="left:607px;top:2014px">03.</div>
<div class="abs step-title" style="left:609px;top:2063px">Trees are kiln dried</div>
<div class="abs step-text" style="left:609px;top:2097px">Lorem ipsum dolor sitnsectetur adipiscing elit, sed do eiusmod tempor incididunt ut labore et.</div>

<div class="abs step-circle" style="left:922px;top:1975px"><div class="step-icon" role="img" aria-label="Finished table"></div></div>
<div class="abs step-num" style="left:868px;top:2076px">04.</div>
<div class="abs step-title" style="left:864px;top:2115px">Lumber to furniture</div>
<div class="abs step-text" style="left:864px;top:2149px">Lorem ipsum dolor sitnsectetur adipiscing elit, sed do eiusmod tempor incididunt ut labore et.</div>

<!-- newsletter -->
<h2 class="abs section-title serif" style="top:2346px"><span class="accent">Newsletter</span> <span class="navy">Signup</span></h2>
<p class="abs news-text">Ed ut perspiciatis unde omnis iste natus error sit accusantium doloremque laudantium, totam rem aperiam, eaque ipsa quae ab illo inventore veritatis et quasi architecto beatae .</p>
<div class="abs email">Email ID</div>
<div class="abs btn submit">Submit</div>

<!-- footer -->
<footer class="abs footer"></footer>
<div class="abs footer-logo"><i></i>Heartwood Tables</div>

<div class="abs footer-head" style="left:498px;top:2642px">CONTACT</div>
<div class="abs contact-line" style="left:498px;top:2692px">
  <svg viewBox="0 0 24 24"><path d="M6.6 10.8a15 15 0 0 0 6.6 6.6l2.2-2.2a1 1 0 0 1 1-.25 11.4 11.4 0 0 0 3.6.57 1 1 0 0 1 1 1V20a1 1 0 0 1-1 1A17 17 0 0 1 3 4a1 1 0 0 1 1-1h3.5a1 1 0 0 1 1 1c0 1.25.2 2.45.57 3.57a1 1 0 0 1-.25 1z"/></svg>+1555-010-0199</div>
<div class="abs contact-line" style="left:498px;top:2726px">
  <svg viewBox="0 0 24 24"><path d="M2 5h20v2l-10 6L2 7zM2 9l10 6 10-6v10H2z"/></svg>info@heartwoodtables.com</div>
<div class="abs contact-line" style="left:498px;top:2760px">
  <svg viewBox="0 0 24 24"><path d="M12 2a7 7 0 0 0-7 7c0 5 7 13 7 13s7-8 7-13a7 7 0 0 0-7-7zm0 9.5A2.5 2.5 0 1 1 12 6.5a2.5 2.5 0 0 1 0 5z"/></svg>Heartwood Tables LLC,</div>
<div class="abs contact-line" style="left:517px;top:2790px">Address comes here</div>

<div class="abs footer-head" style="left:787px;top:2642px">QUICK LINKS</div>
<ul class="abs footer-list" style="left:787px;top:2692px;line-height:30px">
  <li>Home</li><li>Shop</li><li>About</li><li>Contact</li>
</ul>

<div class="abs footer-head" style="left:976px;top:2642px">TERMS</div>
<ul class="abs footer-list" style="left:976px;top:2692px;line-height:30px">
  <li>General Terms</li><li>Security Policy</li><li>Privacy Policy</li>
</ul>

<div class="abs copyright">2023 Heartwood Tables LLC. All Rights Reserved.</div>

</body>
</html>
```